Letterhead Design Project

Initially, we would like to review our letterheads.

Something simple which uses our corporate imagery well and is nicely balanced.

Please note that I will be following up this letter-head with some customised quote templates and similarly customisable collateral in the next few weeks.

Target Market(s)

Enterprise business

Industry/Entity Type

Quote

Requirements
Must have
• The Norbix7 logo
See www.norbix7.com.au

Our tagline "Enterprise Hosting, Messaging and Server Virtualisation"

Our website address

Ideally in our colour pallette, but will consider submissions which look fantastic and necessitate other colours.

```html
<!DOCTYPE html>
<html lang="en">
<head>
<meta charset="utf-8">
<title>Norbix7 Letterhead</title>
<link rel="stylesheet" href="https://fonts.googleapis.com/css2?family=Arimo:wght@400;700&display=swap">
<style>
  :root {
    --paper: #ffffff;
    --ink: #111111;
    --brand-red: #d3121a;
    --red-dark: #8e0d10;
    --band-grey: #dcdcdc;
    --footer-dark: #151515;
    --footer-mid: #3a3a3a;
    --footer-light: #4a4a4a;
    --white: #ffffff;
  }
  html, body {
    margin: 0;
    padding: 0;
    overflow: hidden;
    background: var(--paper);
  }
  .letterhead {
    position: relative;
    width: 860px;
    height: 1200px;
    background: var(--paper);
    overflow: hidden;
    font-family: "Arimo", Arial, sans-serif;
  }
  .brand {
    position: absolute;
    left: 70px;
    top: 72px;
    height: 38px;
    display: flex;
    align-items: center;
    gap: 10px;
  }
  .brand-square {
    width: 38px;
    height: 38px;
    background: var(--brand-red);
  }
  .brand-name {
    font-weight: 700;
    font-size: 36px;
    line-height: 1;
    color: var(--ink);
    letter-spacing: -0.5px;
  }
  .tagline-band {
    position: absolute;
    left: 0;
    top: 1072px;
    width: 860px;
    height: 19px;
    background: var(--band-grey);
  }
  .tagline {
    position: absolute;
    left: 0;
    width: 600px;
    top: 0;
    margin: 0;
    text-align: center;
    font-weight: 700;
    font-size: 16px;
    line-height: 19px;
    color: var(--ink);
  }
  .footer-bar {
    position: absolute;
    left: 0;
    top: 1091px;
    width: 860px;
    height: 109px;
    background: linear-gradient(90deg, var(--footer-dark) 0%, var(--footer-mid) 55%, var(--footer-light) 100%);
  }
  .footer-bar::after {
    content: "";
    position: absolute;
    left: 0; right: 0; top: 0;
    height: 30px;
    background: linear-gradient(180deg, rgba(0,0,0,0.35), rgba(0,0,0,0));
  }
  .footer-accent {
    position: absolute;
    left: 0;
    top: 0;
  }
  .website {
    position: absolute;
    right: 52px;
    top: 45px;
    margin: 0;
    font-weight: 700;
    font-size: 18px;
    color: var(--white);
    z-index: 1;
  }
</style>
</head>
<body>
  <div class="letterhead">
    <header class="brand">
      <span class="brand-square"></span>
      <span class="brand-name">Norbix7</span>
    </header>

    <footer>
      <div class="tagline-band">
        <p class="tagline">Enterprise Hosting, Messaging and Server Virtualisation</p>
      </div>
      <div class="footer-bar">
        <svg class="footer-accent" width="190" height="109" viewBox="0 0 190 109" aria-hidden="true">
          <defs>
            <linearGradient id="accentRed" x1="0" y1="0" x2="0" y2="1">
              <stop offset="0" stop-color="#c8141a"/>
              <stop offset="1" stop-color="#8e0d10"/>
            </linearGradient>
          </defs>
          <polygon points="0,0 183,0 138,109 0,109" fill="url(#accentRed)"/>
        </svg>
        <p class="website">www.norbix7.com.au</p>
      </div>
    </footer>
  </div>
</body>
</html>
```